Web Design Project Bright Lantern

I am needing a website for a theatre called Bright Lantern Stage School (blstage.com) which has already been purchsed from web nest. (Let me know if you need any other info on that.)We need a website that is professional looking and easy to access. Attached is the logo as well as the business card design. I think it would be nice to have the same type of design that’s on the business card but I am definitely open to other creative ideas. I need the website to be in a format where I can edit it in the future when I need to add classes and events to it. Also, some other things I need are I need are a…
A homepage. On the homepage we would like the motto, “Rise to the spotlight.” Also, the mission statement,
Bright Lantern Stage School strives to help students achieve excellence in performance, while building self-confidence and creativity. The Bright Lantern Stage School has created a fun and safe environment, where students can learn, acquire new skills, and explore their potential through musical theatre. Students not only have the freedom to, but are encouraged to embrace who they are and can lose their fear of judgment from others.
Class Registration Page for the classes- (As well as a coin link option for each if that is possible)
4-6 Musical Theatre
Tuesday’s 4:00PM-5:00PM
January 6th – February 24th
8 Weeks
Cost $160
Curriculum: Moss Harbor
Class info: In MT 4-6 your students will learn the basics of singing, dancing, and acting. A lesson of theatre terminology or technique will be taught each week as well as working on the show that will be performed at the end of the 8 weeks semester.

6-9 Musical Theatre
Tuesday’s 5:15PM-6:45PM
January 6th- February 24th
8 Weeks
Cost: $200
Curriculum: Tilly
Class info: In MT 6-9 your students will learn the basics of singing, dancing, and acting. A lesson of theatre terminology or technique will be taught each week as well as working on the show that will be performed at the end of the 8 weeks semester.
9-12 Musical Theatre
Wednesday’s 5:00-7:00PM
8 Weeks
Cost: $240
Curriculum: Gilded
Class info: In MT 9-12 your students will learn intermediate levels of singing, dancing, and acting. A lesson of theatre terminology or technique will be taught each week as well as working on the show that will be performed at the end of the 8 weeks semester.

About- (Include headshot that is attached)
A native Coloradan, Maren is an actress, director, teacher, and wife. She was a Dean’s List graduate of Northridge College in Florida, she holds a B.S. degree in Theatre. Her Capstone Project involved writing, producing, directing, and starring in a 60-minute one-woman musical which was noted by the Chairman of Theatre as setting new standard for the NRC project. Initially attending Harmon College, Maren was one of nine students representing HC at the Great Plains Drama Festival. Maren has also been a senior theatre director at the Maplewood Youth Playhouse for 4 years, where she directed fall, spring, and summer classes for ages 4-19. Her experience includes directing the main stage production, Quill Jr., assistant director for, Keep Your Chin Up Milo Barnes, and stage management for Der Nachtvogel.

Contact us
Phone: 303-555-0147
Email: blstageschool.com

Also, I do not have any photos of students yet so it's ok if their aren't many pictures because I intend on adding some when things get going, so if it's simple that's great. Also, if you find any musical theatre pictures that don't include faces, are just bodies or feet, that would work as well.
Updates

The web address needs to be blstage.com. I have already purchased the domain name from WebNest. Let me know if there are any steps I might be missing or any other info I need to provide. Also, I need to be able to edit the website in the future but I'm not sure which format is best for that.

Target Market(s)

Theatre parents and students

Industry/Entity Type

Building

Requirements
Must have
• Stated above.

```html
<!DOCTYPE html>
<html lang="en">
<head>
<meta charset="utf-8">
<title>About – Bright Lantern Stage School</title>
<link href="https://fonts.googleapis.com/css2?family=Bellefair&family=Cormorant+Garamond:ital,wght@1,400&display=swap" rel="stylesheet">
<style>
  :root {
    --brand-red: #9b0d0d;
    --ink: #1f1f1f;
    --muted: #7a7a7a;
    --soft-ink: #4a4a4a;
    --rule: #d6d6d6;
    --page: #ffffff;
  }
  * { margin: 0; padding: 0; box-sizing: border-box; }
  html, body { width: 1200px; height: 1000px; overflow: hidden; background: var(--page); }
  body {
    position: relative;
    font-family: "Bellefair", serif;
    color: var(--ink);
    border-top: 4px solid var(--brand-red);
    border-bottom: 4px solid var(--brand-red);
  }
  .brand {
    position: absolute;
    display: flex;
    align-items: center;
    gap: 10px;
    font-family: "Bellefair", serif;
    font-size: 30px;
    color: var(--ink);
    white-space: nowrap;
  }
  .brand-mark { width: 14px; height: 14px; background: var(--brand-red); }
  .site-header .brand { left: 263px; top: 60px; }
  .main-nav {
    position: absolute;
    top: 66px;
    left: 616px;
    display: flex;
    gap: 49px;
    font-size: 23px;
  }
  .main-nav a { color: var(--muted); text-decoration: none; padding-bottom: 1px; }
  .main-nav a.is-current { color: var(--ink); border-bottom: 2px solid var(--brand-red); }
  .headshot {
    position: absolute;
    left: 99px; top: 169px;
    width: 288px; height: 391px;
    background: linear-gradient(160deg, #9a9a9a 0%, #5e5e5e 45%, #d8d8d8 100%);
  }
  .bio {
    position: absolute;
    left: 454px; top: 168px;
    width: 650px;
    font-size: 21px;
    line-height: 25px;
  }
  .bio p + p { margin-top: 25px; }
  .rule { position: absolute; height: 1px; background: var(--rule); }
  .rule-contact { left: 291px; top: 620px; width: 618px; }
  .rule-footer { left: 100px; top: 841px; width: 1000px; }
  .contact-title {
    position: absolute;
    left: 523px; top: 652px;
    font-family: "Cormorant Garamond", serif;
    font-style: italic;
    font-weight: 400;
    font-size: 42px;
    color: #333;
  }
  .contact-list {
    position: absolute;
    left: 461px; top: 720px;
    display: grid;
    grid-template-columns: 116px auto;
    font-size: 28px;
    line-height: 31px;
    color: var(--soft-ink);
  }
  .site-footer .brand { left: 50%; transform: translateX(-50%); top: 900px; }
</style>
</head>
<body>
  <header class="site-header">
    <div class="brand"><span class="brand-mark"></span>Bright Lantern Stage School</div>
    <nav class="main-nav">
      <a href="#">Home</a>
      <a href="#">Registration</a>
      <a href="#" class="is-current">About</a>
    </nav>
  </header>

  <main>
    <div class="headshot" role="img" aria-label="Black and white headshot of Maren, the school's director"></div>
    <section class="bio">
      <p>A native Coloradan, Maren is an actress, director, teacher, and wife. She was a Dean’s List graduate of Northridge College in Florida, she holds a B.S. degree in Theatre. Her Capstone Project involved writing, producing, directing, and starring in a 60-minute one-woman musical which was noted by the Chairman of Theatre as setting new standard for the NRC project.</p>
      <p>Initially attending Harmon College, Maren was one of nine students representing HC at the Great Plains Drama Festival. Maren has also been a senior theatre director at the Maplewood Youth Playhouse for 4 years, where she directed fall, spring, and summer classes for ages 4-19.</p>
      <p>Her experience includes directing the main stage production, Quill Jr., assistant director for, Keep Your Chin Up Milo Barnes, and stage management for Der Nachtvogel.</p>
    </section>

    <div class="rule rule-contact"></div>
    <h2 class="contact-title">Contact us</h2>
    <dl class="contact-list">
      <dt>Phone</dt><dd>303-555-0147</dd>
      <dt>Email</dt><dd>blstageschool@inboxmail.net</dd>
    </dl>
    <div class="rule rule-footer"></div>
  </main>

  <footer class="site-footer">
    <div class="brand"><span class="brand-mark"></span>Bright Lantern Stage School</div>
  </footer>
</body>
</html>
```